We require a portrait style A4 flyer. Title is the project name: Protect your most important asset!
To include: use the umbrella family image attached (or another image that you may suggest that portrays family, income protection, and etc on the flyer), photo of financial adviser, name, mobile, email and website details,
please insert the Advice Process shown on page 2 of the Harbourline Financial Solutions brochure attached (please condense its size), please also insert the right hand bullet points (5 of them) from the Life Insurance Fact Sheet attached on page 1 but omit the word "life" and only use "insurance", on the flyer; and then "Why use Harbourline Financial Solutions?" bullet points for this are: please refer to our website for this www.harbourlinefs.com.au . Please use the colour scheme of the Harbourline Financial Solutions logo for the flyer. We would like something simple and easy to read.

```html
<!DOCTYPE html>
<html lang="en">
<head>
<meta charset="utf-8">
<title>Harbourline Financial Solutions – Protect Your Most Important Asset</title>
<link rel="stylesheet" href="https://fonts.googleapis.com/css2?family=Cabin:wght@400;500;600&family=Questrial&display=swap">
<style>
  :root {
    --blue-light: #2258a8;
    --blue-dark: #0b2766;
    --green: #0e9445;
    --green-text: #16893c;
    --grey-bg: #f1f1f1;
    --ink: #3a3a3a;
    --white: #ffffff;
    --url-tint: #cfd8ea;
  }
  * { margin: 0; padding: 0; box-sizing: border-box; }
  html, body { width: 931px; height: 1200px; overflow: hidden; background: var(--white); }
  body { font-family: "Cabin", sans-serif; color: var(--ink); }
  .flyer { position: relative; width: 931px; height: 1200px; overflow: hidden; }
  .backdrop { position: absolute; inset: 0; }

  .brand { position: absolute; left: 30px; top: 40px; display: flex; align-items: center; gap: 16px; }
  .brand-dot { width: 64px; height: 64px; border-radius: 50%; background: var(--white); flex: none; }
  .brand-name { font-family: "Questrial", sans-serif; color: var(--white); font-size: 31px; line-height: 28px; }

  .site-url { position: absolute; right: 52px; top: 68px; font-family: "Questrial", sans-serif; font-size: 23px; letter-spacing: 3px; color: var(--url-tint); }

  .family-photo { position: absolute; left: 405px; top: 140px; width: 500px; height: 428px;
    background: radial-gradient(ellipse at 60% 45%, #e8b9c8 0%, #d9c2b6 35%, #c9d3e0 60%, rgba(241,241,241,0) 78%); }

  .headline { position: absolute; left: 26px; top: 247px; color: var(--white); font-weight: 600; font-size: 26px; line-height: 32px; }

  .step h3 { color: var(--green-text); font-weight: 600; font-size: 13.5px; line-height: 16px; margin-bottom: 2px; }
  .step p { font-size: 11.6px; line-height: 13.9px; text-align: justify; letter-spacing: -0.1px; }
  .step-intro { position: absolute; left: 29px; top: 424px; width: 366px; }
  .process { position: absolute; left: 29px; top: 594px; width: 366px; }
  .process .step + .step { margin-top: 9px; }

  .why { position: absolute; left: 487px; top: 620px; width: 430px; color: var(--white); }
  .why h2 { font-weight: 600; font-size: 19px; margin-bottom: 10px; }
  .why ul { list-style: none; font-size: 15.3px; line-height: 32.2px; }
  .why li::before { content: "• "; font-size: 11px; }
  .why li .cont { display: block; padding-left: 8px; }
  .why-ref { position: absolute; left: 471px; top: 938px; width: 460px; text-align: center; color: var(--white); font-weight: 600; font-size: 16.5px; line-height: 29px; }

  .contact { position: absolute; right: 24px; top: 1075px; text-align: right; color: var(--white); }
  .contact h2 { font-weight: 500; font-size: 23px; margin-bottom: 10px; }
  .contact p { font-family: "Questrial", sans-serif; font-size: 16.5px; line-height: 26px; display: flex; align-items: center; justify-content: flex-end; gap: 8px; }
  .contact svg { width: 14px; height: 14px; }

  .social { position: absolute; left: 29px; top: 1157px; display: flex; gap: 4px; }
  .social span { width: 26px; height: 26px; background: var(--blue-light); border: 1px solid #5b83c4; }
</style>
</head>
<body>
<div class="flyer">
  <svg class="backdrop" width="931" height="1200" viewBox="0 0 931 1200" aria-hidden="true">
    <defs>
      <linearGradient id="band" x1="0" y1="0" x2="1" y2="0">
        <stop offset="0" stop-color="#2258a8"/>
        <stop offset="1" stop-color="#0b2766"/>
      </linearGradient>
    </defs>
    <rect x="0" y="166" width="931" height="417" fill="#f1f1f1"/>
    <path d="M0 0 H931 V113 H507 L440 166 H0 Z" fill="url(#band)"/>
    <polyline points="0,168 441,168 508,115 931,115" fill="none" stroke="#0e9445" stroke-width="3"/>
    <path d="M0 232 H403 L420 330 H0 Z" fill="#0e9445"/>
    <rect x="471" y="583" width="460" height="477" fill="#0e9445"/>
    <path d="M0 1114 H432 L498 1060 H931 V1200 H0 Z" fill="url(#band)"/>
    <polyline points="0,1112 431,1112 497,1058 931,1058" fill="none" stroke="#2e6cc0" stroke-width="2"/>
  </svg>

  <div class="brand">
    <span class="brand-dot"></span>
    <div class="brand-name">Harbourline<br>Financial<br>Solutions</div>
  </div>
  <div class="site-url">www.harbourlinefs.com.au</div>

  <div class="family-photo" role="img" aria-label="Photo of a smiling family of four sitting together under a pink umbrella"></div>

  <h1 class="headline">PROTECT YOUR<br>MOST IMPORTANT ASSET!</h1>

  <section class="step step-intro">
    <h3>Initial Meeting - Discussing Your Aspirations</h3>
    <p>We work with you to establish your current financial situation and help you determine your short and long term financial goals and aspirations; and the likelihood of achieving them. The initial meeting provides a platform for both you and the adviser to exchange information and lay the foundation for establishing your financial goals and objectives. We also perform our data collection and information gathering at this stage. Timeframe: 1-2 Hours.</p>
  </section>

  <div class="process">
    <section class="step">
      <h3>Our Research and Assessment</h3>
      <p>We will analyse your current position such as assets, liabilities, insurance cover and income. We will then evaluate alternatives based on personal values, attitudes to risk, timeframes and economic/enviromental factors. From here, we will develop and compare appropriate strategies; select suitable strategies, services and/or financial products that will assist you in achieving your goals. Timeframe: 2 - 4 Weeks.</p>
    </section>
    <section class="step">
      <h3>Develop and Present Your Plan</h3>
      <p>We will read through your strategic recommendations and provide you with your personalised Statement of Advice document. We will re-cap on your goals. We will discuss our findings in relation to your current situation and goals and whether they can be met. We will answer any questions you may have. Timeframe: 1-2 hours.</p>
    </section>
    <section class="step">
      <h3>Implementation of Your Plan</h3>
      <p>If you have decided to proceed with all or part of our recommendations, we will then work with you in implementing your financial plan in a timely and effective manner. This includes completing any product, investment and insurance applications if applicable. We will then follow up and monitor the implementation process for you, such as following up on any insurance requirements or status of investments being placed. Timeframe: 6-8 weeks from initial appointment.</p>
    </section>
    <section class="step">
      <h3>Ongoing Review and Annual Health Check</h3>
      <p>It is important you review your financial goals to ensure you stay on track to achieve them. We will assess the impact of any change in circumstances and make changes where necessary, such as re-balancing your portfolio or revisiting your insurances. We will address any legislative or economic changes which may affect you.</p>
    </section>
  </div>

  <section class="why">
    <h2>Why use Harbourline Financial Solutions?</h2>
    <ul>
      <li>Paying your medical bills and funeral expenses</li>
      <li>Eliminating your mortgage and other debts (including<span class="cont">business debt if you’re self-employed)</span></li>
      <li>Providing for household bills and everyday living expenses</li>
      <li>Providing for the future education costs for your children</li>
      <li>Adding cash to your estate so it can be divided equitably<span class="cont">without the need to sell assets.</span></li>
    </ul>
  </section>
  <p class="why-ref">please refer to our website for this<br>www.harbourlinefs.com.au</p>

  <section class="contact">
    <h2>CONTACT US</h2>
    <p>3100 4520
      <svg viewBox="0 0 14 14" aria-hidden="true"><path d="M1 5 Q7 0 13 5 L11 6.5 L9.5 5 H4.5 L3 6.5 Z M3 8 H11 V12 H3 Z" fill="#fff"/></svg></p>
    <p>0400 555 182
      <svg viewBox="0 0 14 14" aria-hidden="true"><rect x="3.5" y="1" width="7" height="12" rx="1.2" fill="none" stroke="#fff" stroke-width="1.4"/></svg></p>
    <p>adviser@harbourlinefs.com.au
      <svg viewBox="0 0 14 14" aria-hidden="true"><path d="M1.5 5 L7 1.5 L12.5 5 V12.5 H1.5 Z M1.5 5 L7 9 L12.5 5" fill="none" stroke="#fff" stroke-width="1.3"/></svg></p>
  </section>

  <div class="social" aria-label="Social media links">
    <span></span><span></span><span></span>
  </div>
</div>
</body>
</html>
```